Harlow Stonefield Civil Construction website design

We want a Bold website to promote our Heavy Civil Construction company, We would like an organic / tangible feel to the site. The pictures will be over saturated so they pop. We need to be able to easliy upload new projects and pictures on a regular basis.
Home page will have a full screen width image, "home page image" with silhouette and logo. It will also have about us area and picture
Page 2 will be Project Gallery with pictures in project folders
Page 3 will be an employment application form and submission
Page 4 will be Contact Us
Target Market(s)
Construction indusrty
Industry/Entity Type
Contractor
Coding
Coded - Design and coding required
Number of Pages Required
4 page
Font styles to use
Other font styles liked:
- Hypatia Sans Pro Light
Look and feel

```html
<!DOCTYPE html>
<html lang="en">
<head>
<meta charset="utf-8">
<title>Harlow Stonefield Civil Construction</title>
<link rel="stylesheet" href="https://fonts.googleapis.com/css2?family=Roboto:wght@300;400;500;700&display=swap">
<style>
:root{
  --blue:#30489c;
  --blue-dark:#24397f;
  --ink:#222;
  --text:#666;
  --line:#e2e2e2;
  --light:#f5f5f5;
  --footer:#1d1d1f;
  --footer-bottom:#141415;
  --earth:#7a6a52;
  --earth-dark:#4b3f30;
  --sky:#8fb4d8;
  --machine:#e3b21e;
}
*{box-sizing:border-box;margin:0;padding:0}
html,body{width:1200px;height:4036px;overflow:hidden}
body{font-family:"Roboto",Arial,sans-serif;color:var(--ink);background:#fff;position:relative}
.abs{position:absolute}
a{color:inherit;text-decoration:none}
.btn{display:inline-block;background:var(--blue);color:#fff;font-size:15px;font-weight:500;padding:12px 32px;border-radius:22px}
.photo{position:absolute}

/* top bar */
.topbar{top:0;left:0;width:1200px;height:36px;background:#f1f1f1;font-size:13px;color:#555}
.topbar .contact{position:absolute;left:80px;top:10px;display:flex;gap:48px}
.topbar .contact span{display:flex;align-items:center;gap:8px}
.topbar .social{position:absolute;right:40px;top:0;display:flex;gap:2px}
.topbar .social i{display:block;width:36px;height:36px;background:var(--blue)}
.topbar .social i:nth-child(n+2){background:#fff;border-left:1px solid var(--line)}

/* header */
.header{top:36px;left:0;width:1200px;height:116px;background:#fff}
.logo{position:absolute;display:flex;align-items:center;gap:12px}
.logo .mark{width:42px;height:42px;background:var(--blue)}
.logo .name{font-size:17px;font-weight:700;line-height:1.15;color:var(--blue-dark);text-transform:uppercase;letter-spacing:.5px}
.header .logo{left:80px;top:34px}
.nav{position:absolute;right:60px;top:0;height:116px;display:flex;align-items:center;gap:36px;font-size:15px;color:#444}
.nav a.active{color:var(--blue);position:relative}
.nav a.active::before{content:"";position:absolute;left:-6px;right:-6px;top:-44px;height:3px;background:var(--blue)}

/* hero */
.hero{top:152px;left:0;width:1200px;height:528px;background:linear-gradient(180deg,#8aa6c0 0%,#b7b2a0 34%,#7a6a52 60%,#5a4b38 100%)}
.hero-text{position:absolute;left:0;width:1200px;top:224px;text-align:center;color:#fff}
.hero-text h1{font-size:38px;font-weight:500;line-height:1.35;text-shadow:0 2px 6px rgba(0,0,0,.4)}
.hero-text .btn{margin-top:16px;padding:9px 26px;font-size:14px}
.arrow{position:absolute;top:388px;width:26px;height:26px;border-radius:50%;background:rgba(0,0,0,.45)}
.dots{position:absolute;top:632px;left:572px;display:flex;gap:8px}
.dots i{width:8px;height:8px;border-radius:50%;background:rgba(255,255,255,.6)}
.dots i:first-child{background:#fff}

/* services */
.services{top:752px;left:80px;width:1040px;height:320px;display:flex;gap:24px}
.service{flex:1;text-align:center;padding-top:36px;color:var(--ink)}
.service svg{width:96px;height:96px}
.service h3{font-size:20px;font-weight:500;margin:20px 0 10px}
.service p{font-size:13px;line-height:1.45;color:var(--text);padding:0 34px}
.service.featured{background:var(--blue);color:#fff}
.service.featured p{color:#dfe4f3}

/* about */
.about-photo{top:1088px;left:80px;width:520px;height:412px;background:linear-gradient(160deg,#7fa9d6 0%,#b8cbd6 30%,#c9a43c 52%,#6e5f45 78%,#4d4233 100%)}
.about-text{top:1120px;left:640px;width:480px}
.section-title{font-size:40px;font-weight:500;color:var(--ink)}
.rule{width:70px;height:3px;background:var(--blue);margin:12px 0 28px}
.about-text h4{font-size:19px;font-weight:500;margin-bottom:14px}
.about-text p{font-size:13.5px;line-height:1.6;color:var(--text);margin-bottom:14px}
.about-text .btn{margin-top:10px}

/* heavy civil */
.civil{top:1580px;left:0;width:1200px;height:500px;background:linear-gradient(170deg,#a7a59c 0%,#8b7d66 40%,#6f6048 70%,#544735 100%)}
.civil-card{top:1640px;left:80px;width:460px;height:340px;background:#fff;padding:36px 32px;box-shadow:0 4px 14px rgba(0,0,0,.2)}
.civil-card h2{font-size:38px;font-weight:400;line-height:1.15}
.civil-card .rule{margin:12px 0 20px}
.civil-card p{font-size:13.5px;line-height:1.55;color:var(--text);margin-bottom:12px}
.civil-card .btn{padding:9px 26px;font-size:14px}

/* projects */
.center-title{left:0;width:1200px;text-align:center;font-size:40px;font-weight:500}
.grid{left:80px;width:1040px;display:grid;grid-template-columns:repeat(3,1fr);gap:28px 24px}
.tile{height:264px;position:relative}
.t1{background:linear-gradient(160deg,#8a9a5a,#6d5e44 60%,#4e4433)}
.t2{background:linear-gradient(160deg,#6b6048,#8f7a55 50%,#3d3528)}
.t3{background:linear-gradient(160deg,#a0c3e6,#7c9a62 45%,#c7a13a 65%,#5a4d3b)}
.t4{background:linear-gradient(160deg,#b9d0e8,#5e7fa8 40%,#485a6e 70%,#3a3a3a)}
.t5{background:linear-gradient(160deg,#3e4a2e,#2b3021 60%,#1e2217)}
.t6{background:linear-gradient(160deg,#5a5143,#7a6b54 50%,#3a342b)}
.tile .caption{position:absolute;left:26px;bottom:24px;color:#fff}
.tile .caption h5{font-size:20px;font-weight:400;margin-bottom:6px}
.tile .caption p{font-size:12.5px;line-height:1.45;width:220px;color:#ddd}
.center-btn{left:0;width:1200px;text-align:center}
.center-btn .btn{padding:9px 28px;font-size:14px}

/* blogs */
.blogs{top:2952px;left:80px;width:1040px;display:flex;gap:40px}
.post{flex:1;background:#fff;box-shadow:0 2px 10px rgba(0,0,0,.14);height:376px}
.post .img{height:210px}
.b1{background:linear-gradient(160deg,#6e9ed0,#5a8a6a 45%,#7a7a78 75%,#4a5a6a)}
.b2{background:linear-gradient(160deg,#93b0c8,#a89c80 40%,#6b5d45 75%,#8a7a5e)}
.b3{background:linear-gradient(160deg,#a7c6e4,#4f8a5a 40%,#2f9a88 70%,#3b6a4a)}
.post .meta{display:flex;justify-content:space-between;font-size:11.5px;color:#888;padding:14px 18px 12px;border-bottom:1px solid var(--line)}
.post .meta span{display:flex;gap:14px}
.post h5{font-size:16px;font-weight:500;padding:14px 18px 6px}
.post p{font-size:12.5px;line-height:1.45;color:var(--text);padding:0 18px}
.post .more{font-size:12px;color:#555;padding:10px 18px}

/* newsletter */
.newsletter{top:3460px;left:0;width:1200px;height:212px;background:linear-gradient(180deg,#fff 0%,#f7f7f9 45%,#e8e9ee 100%)}
.newsletter h3{position:absolute;top:28px;width:1200px;text-align:center;font-size:28px;font-weight:500}
.newsletter .form{position:absolute;top:76px;left:320px;display:flex}
.newsletter .field{width:428px;height:36px;border:1px solid #ddd;border-radius:18px 0 0 18px;background:#fff;font-size:13px;color:#999;padding:10px 20px}
.newsletter .submit{width:140px;height:36px;background:var(--blue);color:#fff;font-size:13px;font-weight:700;text-align:center;line-height:36px;border-radius:0 18px 18px 0}
.skyline{position:absolute;left:0;bottom:0;width:1200px;height:90px;background:linear-gradient(180deg,rgba(210,212,222,0) 0%,rgba(196,198,210,.7) 100%)}

/* footer */
.footer{top:3672px;left:0;width:1200px;height:288px;background:var(--footer);color:#bbb}
.footer .logo{left:80px;top:40px}
.footer .logo .mark{background:#fff}
.footer .logo .name{color:#fff}
.footer .about{position:absolute;left:80px;top:110px;width:200px;font-size:13px;line-height:1.5}
.footer .about .read{display:block;margin-top:6px;color:#fff}
.fcol{position:absolute;top:44px}
.fcol h6{font-size:15px;font-weight:500;color:#fff}
.fcol .rule{width:40px;height:2px;margin:8px 0 16px}
.fcol ul{list-style:none;font-size:13px;line-height:1.65}
.fcol ul li::before{content:"› ";color:#888}
.contact-rows{font-size:13px;line-height:1.65;display:grid;grid-template-columns:56px 1fr;column-gap:14px}
.contact-rows b{font-weight:400;color:#fff}
.qform{display:grid;grid-template-columns:1fr 1fr;gap:10px;width:270px}
.qform div{height:28px;background:#2c2c2f;font-size:11.5px;color:#888;padding:7px 10px}
.qform .msg{grid-column:1/3;height:70px}
.qform .send{grid-column:1/2;background:var(--blue);color:#fff;text-align:center;width:90px}
.bottom{top:3960px;left:0;width:1200px;height:76px;background:var(--footer-bottom);font-size:12.5px;color:#999}
.bottom p{position:absolute;left:80px;top:30px}
.bottom .social{position:absolute;right:80px;top:24px;display:flex;gap:12px}
.bottom .social i{display:block;width:28px;height:28px;border-radius:50%;background:#2a2a2e}
.bottom .social i:first-child{background:var(--blue)}
</style>
</head>
<body>

<div class="abs topbar">
  <div class="contact">
    <span><svg width="12" height="12" viewBox="0 0 24 24"><path fill="#30489c" d="M6.6 10.8a15 15 0 006.6 6.6l2.2-2.2c.3-.3.7-.4 1-.2 1.1.4 2.3.6 3.6.6.6 0 1 .4 1 1V20c0 .6-.4 1-1 1A17 17 0 013 4c0-.6.4-1 1-1h3.5c.6 0 1 .4 1 1 0 1.3.2 2.5.6 3.6.1.3 0 .7-.2 1z"/></svg>0800 555 0192</span>
    <span><svg width="13" height="11" viewBox="0 0 24 18"><rect x="1" y="1" width="22" height="16" fill="none" stroke="#30489c" stroke-width="2"/><path d="M1 1l11 9 11-9" fill="none" stroke="#30489c" stroke-width="2"/></svg>hello@harlowstonefield.com</span>
  </div>
  <div class="social"><i></i><i></i><i></i><i></i><i></i></div>
</div>

<header class="abs header">
  <div class="logo"><span class="mark"></span><span class="name">Harlow Stonefield<br>Civil Construction</span></div>
  <nav class="nav">
    <a class="active">Home</a><a>About Us</a><a>Services</a><a>Projects</a><a>Blog</a><a>Careers</a><a>Contact Us</a>
    <svg width="14" height="14" viewBox="0 0 24 24"><circle cx="10" cy="10" r="7" fill="none" stroke="#444" stroke-width="2.5"/><path d="M15 15l7 7" stroke="#444" stroke-width="2.5"/></svg>
  </nav>
</header>

<section class="abs hero" role="img" aria-label="Excavators and dump trucks working on a cleared earthworks site under a blue sky">
  <div class="hero-text">
    <h1>We Are Focused on Build<br>Strong Relations</h1>
    <a class="btn">Get a Quote</a>
  </div>
  <span class="arrow" style="left:28px"></span>
  <span class="arrow" style="right:28px"></span>
  <div class="dots"><i></i><i></i><i></i><i></i></div>
</section>

<section class="abs services">
  <div class="service">
    <svg viewBox="0 0 96 96" fill="none" stroke="#222" stroke-width="3"><path d="M20 82V22h8v60M14 22l14-10 50 10H28M28 22l14 10M66 22v18"/><rect x="58" y="40" width="16" height="10"/><path d="M10 82h36"/></svg>
    <h3>Construction</h3>
    <p>Lorem Ipsum is simply dummy text of the printing and typesetting construction in the industry.</p>
  </div>
  <div class="service featured">
    <svg viewBox="0 0 96 96" fill="none" stroke="#fff" stroke-width="3"><rect x="28" y="14" width="40" height="70"/><path d="M20 84h56M38 26h6M52 26h6M38 38h6M52 38h6M38 50h6M52 50h6M38 62h6M52 62h6M44 84V72h8v12"/></svg>
    <h3>Building</h3>
    <p>Lorem Ipsum is simply dummy text of the printing and typesetting construction in the industry.</p>
  </div>
  <div class="service">
    <svg viewBox="0 0 96 96" fill="#222"><circle cx="48" cy="34" r="11"/><path d="M28 74c0-14 9-22 20-22s20 8 20 22z"/><circle cx="22" cy="40" r="8"/><path d="M6 74c0-11 7-17 16-17 4 0 7 1 9 3-3 4-5 9-5 14z"/><circle cx="74" cy="40" r="8"/><path d="M90 74c0-11-7-17-16-17-4 0-7 1-9 3 3 4 5 9 5 14z"/></svg>
    <h3>Professional Team</h3>
    <p>Lorem Ipsum is simply dummy text of the printing and typesetting construction in the industry.</p>
  </div>
  <div class="service">
    <svg viewBox="0 0 96 96"><circle cx="48" cy="48" r="34" fill="none" stroke="#222" stroke-width="4"/><text x="48" y="58" text-anchor="middle" font-family="Roboto,Arial,sans-serif" font-size="28" font-weight="700" fill="#222">24</text></svg>
    <h3>24/7 support</h3>
    <p>Lorem Ipsum is simply dummy text of the printing and typesetting construction in the industry.</p>
  </div>
</section>

<div class="photo about-photo" role="img" aria-label="Yellow excavator working beside workers on a site with palm trees and blue sky"></div>
<section class="abs about-text">
  <h2 class="section-title">About us</h2>
  <div class="rule"></div>
  <h4>Harlow Stonefield Civil Construction</h4>
  <p>Lorem Ipsum is simply dummy text of the printing and typesetting industry. Lorem Ipsum has been the industry's standard dummy text ever since the 1500s,</p>
  <p>when an unknown printer took a galley of type and scrambled it to make a type specimen book. It has survived not only five centuries, but also the leap into electronic typesetting, remaining essentially unchanged.</p>
  <a class="btn">Read More</a>
</section>

<section class="abs civil" role="img" aria-label="Aerial view of excavators grading a large earthworks site"></section>
<div class="abs civil-card">
  <h2>Heavy Civil<br>Construction</h2>
  <div class="rule"></div>
  <p>Lorem Ipsum is simply dummy a text of the printing and typesetting industry. Ipsum has been the industry.</p>
  <p>when an unknown printer took a galley of type and scram bled it to make a type specimen book. It has survived not only five centuries.</p>
  <a class="btn">Read More</a>
</div>

<h2 class="abs center-title" style="top:2132px">Projects</h2>
<section class="abs grid" style="top:2208px">
  <div class="tile t1" role="img" aria-label="Graded roadway cut with retaining wall"></div>
  <div class="tile t2" role="img" aria-label="Excavator trenching in dark soil"></div>
  <div class="tile t3" role="img" aria-label="Yellow excavator beside a drainage channel"></div>
  <div class="tile t4" role="img" aria-label="Steel framework under construction against the sky"></div>
  <div class="tile t5" role="img" aria-label="Dozer working at a site in low light">
    <div class="caption"><h5>Project Title</h5><p>Lorem Ipsum is simply dummy text of the printing and typesetting.</p></div>
  </div>
  <div class="tile t6" role="img" aria-label="Bulldozer pushing soil on a project site"></div>
</section>
<div class="abs center-btn" style="top:2798px"><a class="btn">View More</a></div>

<h2 class="abs center-title" style="top:2872px">Blogs</h2>
<section class="abs blogs">
  <article class="post">
    <div class="img b1" role="img" aria-label="Aerial view of a highway interchange"></div>
    <div class="meta"><span>June 16, 2019</span><span>20 &nbsp; 12</span></div>
    <h5>Blog Post Title 01</h5>
    <p>Lorem Ipsum is simply dummy the printing and typesetting in the industry.</p>
    <div class="more">Continue...</div>
  </article>
  <article class="post">
    <div class="img b2" role="img" aria-label="Aerial view of road works through a neighbourhood"></div>
    <div class="meta"><span>June 16, 2019</span><span>20 &nbsp; 12</span></div>
    <h5>Blog Post Title 01</h5>
    <p>Lorem Ipsum is simply dummy the printing and typesetting in the industry.</p>
    <div class="more">Continue...</div>
  </article>
  <article class="post">
    <div class="img b3" role="img" aria-label="Excavator working beside a green erosion control slope"></div>
    <div class="meta"><span>June 16, 2019</span><span>20 &nbsp; 12</span></div>
    <h5>Blog Post Title 01</h5>
    <p>Lorem Ipsum is simply dummy the printing and typesetting in the industry.</p>
    <div class="more">Continue...</div>
  </article>
</section>
<div class="abs center-btn" style="top:3376px"><a class="btn">View More</a></div>

<section class="abs newsletter">
  <div class="skyline" role="img" aria-label="Faint city skyline silhouette"></div>
  <h3>Subscribe To Our Newsletter</h3>
  <div class="form"><div class="field">Your E-Mail</div><div class="submit">SUBMIT</div></div>
</section>

<footer class="abs footer">
  <div class="logo"><span class="mark"></span><span class="name">Harlow Stonefield<br>Civil Construction</span></div>
  <div class="about">Lorem Ipsum is simply dummy text of the printing and typesetting in the industry.<a class="read">Read More...</a></div>
  <div class="fcol" style="left:400px">
    <h6>Quick Link</h6><div class="rule"></div>
    <ul><li>Home</li><li>About us</li><li>Services</li><li>Projects</li><li>Blogs</li><li>Careers</li><li>Contact us</li></ul>
  </div>
  <div class="fcol" style="left:560px">
    <h6>Contact us</h6><div class="rule"></div>
    <div class="contact-rows">
      <b>Address</b><span>418 Quarry Road,<br>Ashford, USA<br>Zipcode</span>
      <b>Phone</b><span>+1 555 014 2290</span>
      <b>E-mail</b><span>info@harlowstonefield.com</span>
    </div>
  </div>
  <div class="fcol" style="left:840px">
    <h6>Quick Contact</h6><div class="rule"></div>
    <div class="qform"><div>Name</div><div>Phone</div><div class="msg">Message</div><div class="send">Send</div></div>
  </div>
</footer>
<div class="abs bottom">
  <p>Copyright©2019, Harlow Stonefield Civil Construction. All Rights Reserved.</p>
  <div class="social"><i></i><i></i><i></i><i></i><i></i></div>
</div>

</body>
</html>
```